IT support company needs Banner Ad for the top of their quote layout template

We need a banner Ad for the top of our for quote layout template so it is sent out on all our quotes

The banner size must be 827 x 100 pixels - anything larger than 60 KB can cause upload time issues

We have attached our logo and examples of the quote page to see how it looks in the context of the whole page.

Essential elements of the banner
- Must have our logo but this can be changed to be different colours if it makes the design work better i.e. Tidal Grove could be all in white

Colours
- Can use all of our standard colours - Orange, Black, Grey and White

Images
- As a premium IT support company we deal with people and technology so would like to see both of these Incorporated into the banner i.e. people using technology These images could be watermarked or one colour effect.

Look and Feel
- Professional, friendly, people, technology, premium

Target Market
Small business owners and managers

Industry/Entity Type

It Company

```html
<!DOCTYPE html>
<html lang="en">
<head>
<meta charset="utf-8">
<title>Tidal Grove – Quote Banner</title>
<link rel="stylesheet" href="https://fonts.googleapis.com/css2?family=Exo+2:wght@500;700&display=swap">
<style>
  :root {
    --backdrop: #5f5f5f;
    --panel-light: #f1f1f1;
    --panel-mid: #e6e6e6;
    --brand-orange: #f26a21;
    --brand-orange-light: #ff8c3f;
    --brand-black: #161616;
    --brand-white: #ffffff;
    --photo-cool: #c9cdd3;
    --photo-dark: #4a5566;
  }
  html, body {
    margin: 0;
    padding: 0;
    width: 1200px;
    height: 427px;
    overflow: hidden;
    background: var(--backdrop);
  }
  .banner {
    position: absolute;
    left: 63px;
    top: 169px;
    width: 1006px;
    height: 122px;
    overflow: hidden;
    background: linear-gradient(90deg, var(--panel-mid) 0%, var(--panel-light) 45%);
    font-family: "Exo 2", sans-serif;
  }
  .banner__shapes,
  .banner__photo {
    position: absolute;
    inset: 0;
    width: 100%;
    height: 100%;
  }
  .banner__brand {
    position: absolute;
    left: 22px;
    top: 38px;
    margin: 0;
    font-size: 36px;
    font-weight: 700;
    line-height: 1;
    letter-spacing: 0.5px;
    color: var(--brand-black);
    white-space: nowrap;
  }
  .banner__tagline {
    position: absolute;
    left: 407px;
    top: 35px;
    width: 260px;
    margin: 0;
    text-align: center;
    font-size: 15px;
    font-weight: 500;
    line-height: 22.5px;
    letter-spacing: 0.4px;
    text-transform: uppercase;
    color: var(--brand-white);
  }
</style>
</head>
<body>
  <div class="banner">
    <svg class="banner__photo" viewBox="0 0 1250 152" preserveAspectRatio="none" role="img" aria-label="Faded photograph of business people working with a tablet and laptop at a desk">
      <defs>
        <linearGradient id="photoTone" x1="0" y1="0" x2="1" y2="0">
          <stop offset="0" stop-color="var(--photo-dark)"/>
          <stop offset="0.45" stop-color="#8c95a3"/>
          <stop offset="1" stop-color="var(--photo-cool)"/>
        </linearGradient>
      </defs>
      <polygon points="907,0 1250,0 1250,152 822,152" fill="url(#photoTone)"/>
    </svg>
    <svg class="banner__shapes" viewBox="0 0 1250 152" preserveAspectRatio="none" aria-hidden="true">
      <defs>
        <linearGradient id="orangeBand" x1="0" y1="0" x2="1" y2="0">
          <stop offset="0" stop-color="var(--brand-orange)"/>
          <stop offset="1" stop-color="var(--brand-orange-light)"/>
        </linearGradient>
      </defs>
      <polygon class="accent-stripe" points="502,14 520,14 404,138 386,138" fill="var(--brand-black)"/>
      <polygon class="accent-stripe" points="905,14 922,14 836,152 820,152" fill="var(--brand-black)"/>
      <polygon class="orange-band" points="520,0 907,0 822,152 397,152" fill="url(#orangeBand)"/>
    </svg>
    <p class="banner__brand">Tidal Grove</p>
    <p class="banner__tagline">Bringing enterprise-level solutions to East Anglia small businesses</p>
  </div>
</body>
</html>
```